Consulting company needs Business Cards - rough concept provided

I'm looking for someone to take our business card idea and make is slick and polished - to communicate our high-end, sophisticated, serious consulting business. We have a rough layout we did in-house. We are open to ideas on repo-ing elements, adjusting sizes, typefaces etc... within the general concept we've already come up with. We want it to be super-clean and sophisticated. We want to keep the white backgrounds, and blue brand colors. Our goal is to print with painted blue edges on thick cardstock. Thank you!!

```html
<!DOCTYPE html>
<html lang="en">
<head>
<meta charset="utf-8">
<title>Norward Business Cards</title>
<link href="https://fonts.googleapis.com/css2?family=Inter:wght@300;400;600;800&display=swap" rel="stylesheet">
<style>
  :root {
    --stage-blue: #2190cf;
    --brand-blue: #1f98dc;
    --pale-blue: #d6ecf8;
    --card-white: #fdfdfd;
    --muted-grey: #a8a8a8;
  }
  * { margin: 0; padding: 0; box-sizing: border-box; }
  html, body { width: 1200px; height: 1000px; overflow: hidden; }
  body {
    background: var(--stage-blue);
    font-family: "Inter", Helvetica, Arial, sans-serif;
    position: relative;
  }
  .card {
    position: absolute;
    left: 250px;
    width: 700px;
    height: 400px;
    background: var(--card-white);
    overflow: hidden;
  }
  .card--front { top: 60px; }
  .card--back { top: 540px; }

  /* Front */
  .wordmark {
    position: absolute;
    color: var(--brand-blue);
    font-weight: 800;
    letter-spacing: -0.04em;
    line-height: 1;
    white-space: nowrap;
  }
  .card--front .wordmark { top: 28px; right: 30px; font-size: 96px; }
  .holder { position: absolute; left: 40px; top: 228px; }
  .holder__name { color: var(--brand-blue); font-weight: 800; font-size: 22px; letter-spacing: 0.01em; }
  .holder__role { color: var(--muted-grey); font-weight: 400; font-size: 13px; letter-spacing: 0.28em; margin-top: 4px; }
  .contact {
    position: absolute; left: 400px; top: 222px;
    color: var(--brand-blue); font-size: 17px; line-height: 1.35; font-weight: 400;
    font-style: normal;
  }
  .texture-field {
    position: absolute; left: 40px; top: 300px; width: 320px; height: 70px;
    background: linear-gradient(90deg, var(--pale-blue), #eaf5fc);
  }

  /* Back */
  .rule { position: absolute; left: 40px; width: 620px; height: 6px; }
  .rule--top { top: 40px; }
  .rule--bottom { top: 236px; }
  .promise {
    position: absolute; left: 40px; top: 66px; width: 620px;
    font-size: 26px; line-height: 1.3; color: var(--muted-grey); font-weight: 300;
  }
  .promise strong { color: var(--brand-blue); font-weight: 800; }
  .card--back .wordmark { left: 40px; bottom: 40px; font-size: 80px; }
</style>
</head>
<body>
  <section class="card card--front" aria-label="Business card front">
    <div class="wordmark">NORWARD</div>
    <div class="holder">
      <div class="holder__name">DANA WHITLOCK</div>
      <div class="holder__role">BRAND CONSULTANT</div>
    </div>
    <address class="contact">
      4820 Larkspur Ave, Ste 210<br>
      Maple Ridge, CA 91700<br>
      (555) 014 2290<br>
      dana@norward.com
    </address>
    <div class="texture-field" role="img" aria-label="Field of small blue squares as a brand texture"></div>
  </section>

  <section class="card card--back" aria-label="Business card back">
    <svg class="rule rule--top" viewBox="0 0 620 6" aria-hidden="true">
      <line x1="3" y1="3" x2="620" y2="3" stroke="#1f98dc" stroke-width="6" stroke-dasharray="6 14"/>
    </svg>
    <p class="promise">
      <strong>We help</strong> [target demographic] <strong>achieve</strong> [desired emotional outcome] <strong>by</strong> [our unique approach] <strong>because</strong> [our brand beliefs]
    </p>
    <svg class="rule rule--bottom" viewBox="0 0 620 6" aria-hidden="true">
      <line x1="3" y1="3" x2="620" y2="3" stroke="#1f98dc" stroke-width="6" stroke-dasharray="6 14"/>
    </svg>
    <div class="wordmark">NORWARD.COM</div>
  </section>
</body>
</html>
```